Fernhollow Ridge Farms
letterhead, envelope and business cards
Fernhollow Ridge Farms -
Creative Brief
Traditional
Tessa Harlan
3157 W Birch Mill Road North Platte, NE 68437
sales@fernhollowridgefarms.example
www.fernhollowridgefarms.example

```html
<!DOCTYPE html>
<html lang="en">
<head>
<meta charset="utf-8">
<title>Fernhollow Ridge Farms – Stationery</title>
<link rel="stylesheet" href="https://fonts.googleapis.com/css2?family=Libre+Baskerville:wght@400;700&display=swap">
<style>
  :root{
    --backdrop:#a3a3a3;
    --paper:#ffffff;
    --brown-deep:#2b0b04;
    --brown:#4a1a0a;
    --gold-dark:#9c6a22;
    --gold:#d4a24a;
    --gold-light:#f3d489;
    --ink:#3a1f12;
    --window:#c9c9cf;
  }
  *{margin:0;padding:0;box-sizing:border-box}
  html,body{width:1200px;height:796px;overflow:hidden;background:var(--backdrop)}
  body{position:relative;font-family:"Libre Baskerville",Georgia,serif;color:var(--ink)}
  .piece{position:absolute;background:var(--paper);box-shadow:0 1px 4px rgba(0,0,0,.25);overflow:hidden}
  .piece > svg.art{position:absolute;inset:0;width:100%;height:100%}
  .brand{position:absolute;color:var(--brown);font-weight:700;line-height:1.05;text-align:center;letter-spacing:.02em;z-index:1}
  .small{position:absolute;font-size:8px;line-height:1.45;color:var(--ink);z-index:1}

  .envelope{left:43px;top:149px;width:610px;height:327px}
  .envelope .brand{left:30px;top:112px;font-size:19px;width:160px}
  .envelope .return-address{left:36px;top:188px}
  .envelope .window{position:absolute;left:293px;top:182px;width:209px;height:77px;border-radius:10px;background:var(--window)}

  .letterhead{left:653px;top:41px;width:528px;height:703px}
  .letterhead .brand{right:34px;top:12px;font-size:17px;width:160px}
  .letterhead .footer-rule{position:absolute;left:10px;right:10px;top:650px;height:2px;background:var(--gold)}
  .letterhead .footer{position:absolute;left:0;right:0;top:660px;text-align:center;font-size:7.5px}
  .letterhead .footer-contacts{display:flex;justify-content:center;gap:24px;margin-top:5px}
  .letterhead .footer b{font-weight:700;margin-right:6px}

  .card{width:216px;height:156px;top:533px}
  .card-front{left:120px}
  .card-front .brand{right:10px;top:14px;font-size:11px;width:100px}
  .card-front .holder{left:14px;top:20px;font-size:8.5px;font-weight:700}
  .card-front .contact{left:14px;top:90px;font-size:6px}
  .card-back{left:360px;background:var(--brown-deep)}
  .card-back .brand{left:0;right:0;top:40px;font-size:14px;color:var(--gold-light)}
  .card-back .web{left:0;right:0;bottom:18px;text-align:center;font-size:6.5px;color:var(--gold-light)}
</style>
</head>
<body>

<section class="piece envelope" aria-label="Envelope">
  <svg class="art" viewBox="0 0 610 327" preserveAspectRatio="none">
    <defs>
      <linearGradient id="flap" x1="0" x2="1">
        <stop offset="0" stop-color="#2b0b04"/><stop offset=".5" stop-color="#8a4a1c"/><stop offset="1" stop-color="#2b0b04"/>
      </linearGradient>
      <linearGradient id="goldEnv" x1="0" x2="1">
        <stop offset="0" stop-color="#9c6a22"/><stop offset=".5" stop-color="#f3d489"/><stop offset="1" stop-color="#b07d2e"/>
      </linearGradient>
    </defs>
    <path d="M0 0 H610 V82 L585 90 H25 L0 82 Z" fill="url(#flap)"/>
    <path d="M0 282 C170 230 360 262 470 248 C530 240 575 228 610 218 V327 H0 Z" fill="url(#goldEnv)"/>
    <path d="M0 298 C170 250 360 280 470 266 C530 258 575 248 610 238 V327 H0 Z" fill="#ffffff"/>
  </svg>
  <div class="brand">Fernhollow<br>Ridge Farms</div>
  <p class="small return-address">3157 W Birch Mill Road<br>North Platte, NE 68437</p>
  <div class="window"></div>
</section>

<section class="piece letterhead" aria-label="Letterhead">
  <svg class="art" viewBox="0 0 528 703" preserveAspectRatio="none">
    <defs>
      <linearGradient id="goldLh" x1="0" x2="1">
        <stop offset="0" stop-color="#b07d2e"/><stop offset=".45" stop-color="#f3d489"/><stop offset="1" stop-color="#9c6a22"/>
      </linearGradient>
    </defs>
    <path d="M0 118 C130 136 230 106 320 84 C400 66 460 66 528 78 V60 C460 48 390 48 320 68 C230 92 130 118 0 100 Z" fill="url(#goldLh)"/>
  </svg>
  <div class="brand">Fernhollow<br>Ridge Farms</div>
  <div class="footer-rule"></div>
  <div class="footer">
    <div>3157 W Birch Mill Road, North Platte, NE 68437</div>
    <div class="footer-contacts">
      <span><b>Phone</b>(308) 555-0142</span>
      <span><b>Email</b>sales@fernhollowridgefarms.example</span>
      <span><b>Web</b>www.fernhollowridgefarms.example</span>
    </div>
  </div>
</section>

<section class="piece card card-front" aria-label="Business card front">
  <svg class="art" viewBox="0 0 216 156" preserveAspectRatio="none">
    <defs>
      <linearGradient id="goldCard" x1="0" x2="1">
        <stop offset="0" stop-color="#9c6a22"/><stop offset=".5" stop-color="#f3d489"/><stop offset="1" stop-color="#b07d2e"/>
      </linearGradient>
    </defs>
    <path d="M0 74 C60 58 140 64 216 46 V56 C140 74 60 68 0 84 Z" fill="url(#goldCard)"/>
  </svg>
  <div class="brand">Fernhollow<br>Ridge Farms</div>
  <p class="small holder">Tessa Harlan</p>
  <p class="small contact">3157 W Birch Mill Road<br>North Platte, NE 68437<br><b>Phone</b> (308) 555-0142<br><b>Email</b> sales@fernhollowridgefarms.example</p>
</section>

<section class="piece card card-back" aria-label="Business card back">
  <svg class="art" viewBox="0 0 216 156" preserveAspectRatio="none">
    <path d="M0 108 C70 96 150 104 216 88 V94 C150 112 70 104 0 116 Z" fill="url(#goldCard)"/>
  </svg>
  <div class="brand">Fernhollow<br>Ridge Farms</div>
  <p class="small web">www.fernhollowridgefarms.example</p>
</section>

</body>
</html>
```